Kip's Pharmacy Business Card Design Project

I need a business card designed for my pharmacy Kip's Pharmacy. I would like just the logo on one side, maybe with black background and white lettering. The other side I would also like to include my logo which is attached. Also, please include my name and the following information:
Rolf Mayhew Owner/Pharm D.
Business address is 7314 N Birchwood Rd Sioux Falls, SD 57193.
Phone number is 605-318-2067 and fax # is 605-318-2063.
my email address is kip@kipsrxhall.com.
My website is www.kipsrxhall.com.
My business hours are Monday-Friday 8am-7 pm. Saturday 8am-12 pm. Sunday Closed.
I would like the design to include my logo colors, black, white, and neon green. Silver may be added as a highlight. Thanks.
Industry/Entity Type
Pharmacy
Contact Information for Business Card
See above in product description
Look and feel

```html
<!DOCTYPE html>
<html lang="en">
<head>
<meta charset="utf-8">
<title>Kip's Pharmacy – Business Card</title>
<link rel="stylesheet" href="https://fonts.googleapis.com/css2?family=Josefin+Sans:wght@400;600;700&display=swap">
<style>
  :root {
    --bg: #ecedef;
    --card: #2b2b2c;
    --card-edge: #1f1f20;
    --white: #ffffff;
    --silver: #b9bcc0;
    --neon: #7ed321;
  }
  * { box-sizing: border-box; margin: 0; padding: 0; }
  html, body {
    width: 1200px; height: 800px; overflow: hidden;
    background: var(--bg);
    font-family: "Josefin Sans", sans-serif;
    color: var(--white);
  }
  .sheet {
    width: 1200px; height: 800px;
    display: flex; align-items: center; justify-content: center; gap: 48px;
  }
  .card {
    width: 540px; height: 309px;
    background: var(--card);
    position: relative;
    box-shadow: 0 8px 22px rgba(0,0,0,.18);
  }

  /* Front side */
  .card--front { display: flex; align-items: center; justify-content: center; gap: 26px; }
  .brand-dot { width: 44px; height: 44px; border-radius: 50%; background: var(--neon); }
  .brand-rule { width: 2px; height: 78px; background: var(--silver); }
  .brand-name--large { font-size: 44px; font-weight: 600; color: var(--white); letter-spacing: -.5px; padding-top: 6px; }

  /* Back side */
  .card--back { padding: 22px 26px 20px 26px; }
  .back-header { display: flex; justify-content: space-between; align-items: flex-start; }
  .brand-small { display: flex; align-items: center; gap: 10px; }
  .brand-small .brand-dot { width: 20px; height: 20px; }
  .brand-small .brand-rule { width: 1.5px; height: 36px; }
  .brand-name--small { font-size: 18px; font-weight: 600; padding-top: 3px; }
  .web-contact { text-align: right; font-size: 12px; font-weight: 600; line-height: 1.15; letter-spacing: .3px; }
  .holder { margin-top: 10px; font-size: 18px; font-weight: 700; letter-spacing: .4px; }
  .hours { margin-top: 12px; font-size: 13px; font-weight: 600; line-height: 1.3; list-style: none; }
  .phones { position: absolute; left: 26px; bottom: 18px; font-weight: 600; line-height: .95; }
  .phones .phone { font-size: 20px; letter-spacing: .8px; }
  .phones .fax { font-size: 17px; letter-spacing: .8px; }
  .address { position: absolute; right: 26px; bottom: 22px; font-size: 11px; font-weight: 600; letter-spacing: .3px; }
</style>
</head>
<body>
<main class="sheet">
  <section class="card card--front" aria-label="Card front">
    <span class="brand-dot"></span>
    <span class="brand-rule"></span>
    <span class="brand-name brand-name--large">Kip's Pharmacy</span>
  </section>

  <section class="card card--back" aria-label="Card back">
    <header class="back-header">
      <div class="brand-small">
        <span class="brand-dot"></span>
        <span class="brand-rule"></span>
        <span class="brand-name brand-name--small">Kip's Pharmacy</span>
      </div>
      <div class="web-contact">
        <div>kip@kipsrxhall.com</div>
        <div>www.kipsrxhall.com</div>
      </div>
    </header>
    <h1 class="holder">Rolf Mayhew Owner/Pharm D.</h1>
    <ul class="hours">
      <li>Monday - Friday</li>
      <li>8 AM - 7 PM</li>
      <li>Saturday</li>
      <li>8 AM - 12 PM</li>
      <li>Sunday</li>
      <li>Closed</li>
    </ul>
    <div class="phones">
      <div class="phone">605-318-2067</div>
      <div class="fax">Fax: 605-318-2063</div>
    </div>
    <address class="address" style="font-style:normal">7314 N Birchwood Rd Sioux Falls, SD 57193</address>
  </section>
</main>
</body>
</html>
```